Unique E-commerce website needs a FLAT UI design

Looking for creative website designer / company to design a flat ui interface for the main 4 pages.

I SEEK FLAT UI DESIGN ONLY - this means nice, clean and modern design,

As we're dealing with the design of the main pages this will define the overall site design so take a moment or two to think on the audience and create an appealing branding.

Website design must be mobile/ipad friendly.

I've written a detailed design requirements document for those 4 pages.
Please read it carefully and make sure you understand every aspect of it before starting the design process.
You can find a brief intro text and some reference designs that I like to get you started.

This is not a closed concept, I'm open to hear new ideas and ways to improve the UI/UX.

Feel free to ask anything, I'm available most of the day.

I'm looking to build a long term relationship as this is the first phase of the design, I have 1-2 phases to come.

Target Market(s)

Online shoppers age between 18-60 that buy frequently at US merchants

Industry/Entity Type

It Company

Number of Pages Required

4 page

Requirements
Must have
• Flat UI design
• Flat colors
• Modern, clean and easy to follow design
Nice to have
• Original icons for the features page

```html
<!DOCTYPE html>
<html lang="en">
<head>
<meta charset="utf-8">
<title>ParcelPort – Send &amp; Receive Packages</title>
<link href="https://fonts.googleapis.com/css2?family=Open+Sans:wght@300;400;600;700&display=swap" rel="stylesheet">
<style>
  :root {
    --ink: #222222;
    --muted: #666666;
    --white: #ffffff;
    --hero-dark: #2b2420;
    --hero-mid: #5a4a3c;
    --hero-light: #8a7560;
    --button-blue: #1d4f7a;
    --dark-band: #2b2b2b;
    --lime: #c3d23b;
    --gold: #f2c521;
    --coral: #f07c63;
    --footer-blue: #2391d6;
    --line: #e5e5e5;
  }
  * { box-sizing: border-box; margin: 0; padding: 0; }
  html, body { width: 857px; height: 1200px; overflow: hidden; }
  body { font-family: 'Open Sans', Arial, sans-serif; color: var(--ink); background: var(--white); position: relative; }

  /* Hero */
  .hero { position: absolute; left: 0; top: 0; width: 857px; height: 457px; overflow: hidden; }
  .hero-photo {
    position: absolute; inset: 0;
    background: linear-gradient(100deg, var(--hero-mid) 0%, var(--hero-dark) 40%, var(--hero-dark) 60%, var(--hero-light) 100%);
  }
  .hero-shade { position: absolute; inset: 0; background: rgba(0,0,0,0.35); }
  .site-header {
    position: absolute; left: 0; top: 0; width: 100%; height: 40px;
    background: rgba(0,0,0,0.45);
    display: flex; align-items: center; justify-content: space-between; padding: 0 26px;
  }
  .brand { color: var(--white); font-weight: 700; font-size: 20px; letter-spacing: 0.2px; }
  .main-nav { display: flex; gap: 36px; }
  .main-nav a { color: var(--white); font-size: 12px; text-decoration: none; }
  .hero-content { position: absolute; left: 0; top: 196px; width: 100%; text-align: center; color: var(--white); }
  .hero-title { font-size: 36px; font-weight: 700; letter-spacing: 0.5px; }
  .hero-title span { font-weight: 300; }
  .hero-subtitle { font-size: 26px; font-weight: 300; margin-top: 4px; }
  .signup-form { display: flex; justify-content: center; gap: 32px; margin-top: 36px; }
  .field {
    width: 208px; height: 38px; background: var(--white); border-radius: 3px;
    color: #aaaaaa; font-size: 12px; text-align: left; padding: 11px 14px;
  }
  .create-account {
    display: inline-block; margin-top: 18px; background: var(--button-blue); color: var(--white);
    font-size: 12px; padding: 10px 22px; border-radius: 2px; letter-spacing: 0.3px;
  }

  /* Features */
  .features { position: absolute; left: 0; top: 457px; width: 857px; height: 309px; background: var(--white); }
  .feature-link {
    position: absolute; left: 229px; top: 100px; width: 405px; height: 1px; background: var(--line);
  }
  .feature { position: absolute; top: 42px; width: 170px; text-align: center; }
  .feature-photo {
    width: 114px; height: 114px; border-radius: 50%; margin: 0 auto;
    border: 3px solid var(--white); box-shadow: 0 0 0 1px var(--line);
  }
  .photo-shop { background: linear-gradient(135deg, #3a3a3a, #7fae3a); }
  .photo-delivery { background: linear-gradient(135deg, #9ec5e8, #e8e8e8); }
  .photo-door { background: linear-gradient(135deg, #6b8fb5, #d9d3c8); }
  .feature-title { font-size: 16px; font-weight: 700; margin-top: 20px; }
  .feature-text { font-size: 10.5px; line-height: 15px; color: var(--muted); margin-top: 8px; }
  .read-more { font-size: 10.5px; color: var(--muted); margin-top: 6px; }
  .read-more.active { color: var(--button-blue); text-decoration: underline; }

  /* Pricing */
  .pricing { position: absolute; left: 0; top: 766px; width: 857px; height: 391px; background: var(--dark-band); }
  .plans { position: absolute; left: 137px; top: 42px; display: flex; gap: 0; }
  .plan { width: 194px; height: 315px; position: relative; }
  .plan.lime { background: var(--lime); }
  .plan.gold { background: var(--gold); }
  .plan.coral { background: var(--coral); }
  .plan-icon {
    position: absolute; left: 67px; top: 18px; width: 60px; height: 60px; border-radius: 50%;
    background: rgba(0,0,0,0.12); display: flex; align-items: center; justify-content: center;
  }
  .plan-body {
    position: absolute; left: 10px; top: 92px; width: 174px; height: 190px; background: var(--white);
    text-align: center; padding-top: 18px;
  }
  .plan-name { font-size: 14px; letter-spacing: 0.5px; }
  .plan-price { font-size: 10.5px; color: var(--muted); margin-top: 2px; }
  .plan-features { list-style: none; margin-top: 18px; font-size: 10px; line-height: 19px; color: var(--ink); }
  .plan-signup {
    position: absolute; left: 0; bottom: 0; width: 100%; height: 33px; text-align: center;
    color: var(--white); font-size: 13px; line-height: 33px; letter-spacing: 0.5px;
  }

  /* Footer */
  .site-footer {
    position: absolute; left: 0; top: 1157px; width: 857px; height: 43px; background: var(--footer-blue);
    display: flex; align-items: center; justify-content: space-between; padding: 0 86px;
    color: var(--white); font-size: 11px;
  }
  .social { display: flex; gap: 6px; }
  .social span { width: 17px; height: 17px; background: var(--white); opacity: 0.9; border-radius: 2px; }
</style>
</head>
<body>

<section class="hero">
  <div class="hero-photo" role="img" aria-label="Photo of a courier holding a parcel in a warehouse stacked with boxes"></div>
  <div class="hero-shade"></div>

  <header class="site-header">
    <div class="brand">ParcelPort</div>
    <nav class="main-nav">
      <a href="#">Home</a>
      <a href="#">Our services</a>
      <a href="#">Pricing</a>
      <a href="#">Location</a>
      <a href="#">Contact us</a>
    </nav>
  </header>

  <div class="hero-content">
    <h1 class="hero-title">Send &amp; Receive <span>Packages</span></h1>
    <p class="hero-subtitle">Your One Of The Best 24/7 Post Office</p>
    <div class="signup-form">
      <div class="field">Username</div>
      <div class="field">Password</div>
    </div>
    <div class="create-account">CREATE ACCOUNT</div>
  </div>
</section>

<section class="features">
  <div class="feature-link"></div>

  <div class="feature" style="left:144px">
    <div class="feature-photo photo-shop" role="img" aria-label="Photo of a keyboard with a green shopping key"></div>
    <h2 class="feature-title">Online Shop</h2>
    <p class="feature-text">Shop any US store online and ship your orders to your own address with us, quickly and safely every day.</p>
    <p class="read-more">Read More &rsaquo;</p>
  </div>

  <div class="feature" style="left:321px">
    <div class="feature-photo photo-delivery" role="img" aria-label="Photo of a white delivery van"></div>
    <h2 class="feature-title">Fast Delivery</h2>
    <p class="feature-text">Our team picks up and delivers your parcels on time, with tracking from the store right to your hands.</p>
    <p class="read-more active">Read More &rsaquo;</p>
  </div>

  <div class="feature" style="left:549px">
    <div class="feature-photo photo-door" role="img" aria-label="Photo of a courier handing over a parcel at a door"></div>
    <h2 class="feature-title">Door Step</h2>
    <p class="feature-text">Get every package brought to your door step, signed for and safe, at a time that suits you best.</p>
    <p class="read-more">Read More &rsaquo;</p>
  </div>
</section>

<section class="pricing">
  <div class="plans">
    <article class="plan lime">
      <div class="plan-icon">
        <svg width="28" height="28" viewBox="0 0 28 28"><path d="M3 13 L25 4 L19 24 L13 17 Z" fill="#333"/><path d="M13 17 L25 4" stroke="#c3d23b" stroke-width="1.5"/></svg>
      </div>
      <div class="plan-body">
        <h3 class="plan-name">STARTER</h3>
        <p class="plan-price">$37/Month</p>
        <ul class="plan-features">
          <li>Pay Per Delivery</li>
          <li>Pick Up Anytime</li>
          <li>Secure and Convenient</li>
          <li>Best Services</li>
          <li>First Delivery Free</li>
        </ul>
      </div>
      <div class="plan-signup">SIGN UP</div>
    </article>

    <article class="plan gold">
      <div class="plan-icon">
        <svg width="30" height="26" viewBox="0 0 30 26"><circle cx="15" cy="7" r="4.5" fill="#333"/><circle cx="6" cy="10" r="3.5" fill="#333"/><circle cx="24" cy="10" r="3.5" fill="#333"/><path d="M8 24 Q15 10 22 24 Z" fill="#333"/><path d="M0 23 Q6 12 11 20 L9 23 Z" fill="#333"/><path d="M30 23 Q24 12 19 20 L21 23 Z" fill="#333"/></svg>
      </div>
      <div class="plan-body">
        <h3 class="plan-name">PROFESSIONAL</h3>
        <p class="plan-price">$37/Month</p>
        <ul class="plan-features">
          <li>Pay Per Delivery</li>
          <li>Pick Up Anytime</li>
          <li>Secure and Convenient</li>
          <li>Best Services</li>
          <li>First Delivery Free</li>
        </ul>
      </div>
      <div class="plan-signup">SIGN UP</div>
    </article>

    <article class="plan coral">
      <div class="plan-icon">
        <svg width="28" height="28" viewBox="0 0 28 28"><path d="M24 4 Q14 5 9 14 L14 19 Q23 14 24 4 Z" fill="#333"/><path d="M9 14 L4 15 L7 11 Z M14 19 L13 24 L17 21 Z" fill="#333"/><path d="M7 19 L4 24 L9 21" fill="#333"/></svg>
      </div>
      <div class="plan-body">
        <h3 class="plan-name">PREMIUM</h3>
        <p class="plan-price">$37/Month</p>
        <ul class="plan-features">
          <li>Pay Per Delivery</li>
          <li>Pick Up Anytime</li>
          <li>Secure and Convenient</li>
          <li>Best Services</li>
          <li>First Delivery Free</li>
        </ul>
      </div>
      <div class="plan-signup">SIGN UP</div>
    </article>
  </div>
</section>

<footer class="site-footer">
  <p>Copyrights &copy; 2014 &copy; ParcelPort - All Right Reserved</p>
  <div class="social"><span></span><span></span><span></span><span></span><span></span></div>
</footer>

</body>
</html>
```